Design for supplement packages

We are developing a new supplement brand are looking for a label, based on the design of our naturopath practice. It should include our logo, the basic colors are green, gold and white. www.tessarin-vitalo.de is the practices web site.

Target Market(s)

Europe and North America

Industry/Entity Type

Supplement

Font styles to use
Sans Serif

Colors
acd037
ffffff

Requirements
Should not have
• A too busy design. I like it simple and high class

```html
<!DOCTYPE html>
<html lang="en">
<head>
<meta charset="utf-8">
<title>Naturopath – Supplement Label</title>
<link rel="stylesheet" href="https://fonts.googleapis.com/css2?family=Big+Shoulders+Display:wght@600&family=Libre+Caslon+Text&family=Raleway:wght@400&display=swap">
<style>
  :root {
    --canvas-bg: #eef0f2;
    --label-orange: #b04a00;
    --label-orange-deep: #a23f00;
    --gold-light: #f1dc86;
    --gold-mid: #d9b449;
    --gold-deep: #b8912c;
    --gold-plate: #deb24e;
    --brand-lime: #d8dc6e;
    --tagline-gold: #e7b84a;
    --white: #ffffff;
  }
  * { box-sizing: border-box; margin: 0; padding: 0; }
  html, body {
    width: 1200px;
    height: 800px;
    overflow: hidden;
    background: var(--canvas-bg);
  }
  .canvas {
    position: relative;
    width: 1200px;
    height: 800px;
    display: flex;
    align-items: center;
    justify-content: center;
  }
  .label {
    position: relative;
    width: 560px;
    height: 740px;
    background: linear-gradient(90deg, var(--label-orange) 0%, var(--label-orange) 55%, var(--label-orange-deep) 100%);
    overflow: hidden;
  }
  .foil-band {
    position: absolute;
    left: 0;
    width: 100%;
    background: linear-gradient(100deg, var(--gold-mid) 0%, var(--gold-light) 18%, var(--gold-deep) 38%, var(--gold-light) 58%, var(--gold-mid) 78%, var(--gold-light) 100%);
  }
  .foil-band--top { top: 0; height: 72px; }
  .foil-band--bottom { bottom: 0; height: 88px; }
  .brand {
    position: absolute;
    top: 196px;
    left: 0;
    width: 100%;
    display: flex;
    align-items: center;
    justify-content: center;
    gap: 12px;
  }
  .brand__dot {
    width: 34px;
    height: 34px;
    border-radius: 50%;
    background: var(--brand-lime);
  }
  .brand__name {
    font-family: "Raleway", sans-serif;
    font-weight: 400;
    font-size: 28px;
    color: var(--brand-lime);
    letter-spacing: 0.5px;
  }
  .product-name {
    position: absolute;
    top: 270px;
    left: 0;
    width: 100%;
    text-align: center;
    font-family: "Big Shoulders Display", sans-serif;
    font-weight: 600;
    font-size: 128px;
    line-height: 1;
    color: var(--white);
    letter-spacing: 4px;
  }
  .tagline {
    position: absolute;
    top: 404px;
    left: 0;
    width: 100%;
    text-align: center;
    font-family: "Libre Caslon Text", serif;
    font-size: 14px;
    color: var(--tagline-gold);
    letter-spacing: 0.5px;
  }
  .info-plate {
    position: absolute;
    top: 570px;
    left: 105px;
    width: 315px;
    height: 75px;
    background: var(--gold-plate);
  }
</style>
</head>
<body>
  <main class="canvas">
    <section class="label">
      <div class="foil-band foil-band--top" role="img" aria-label="Crinkled gold leaf foil band"></div>

      <div class="brand">
        <span class="brand__dot"></span>
        <span class="brand__name">Tessarin Vitalo</span>
      </div>

      <h1 class="product-name">NATUROPATH</h1>
      <p class="tagline">RESTORING + MAINTAINING OPTIMAL HEALTH</p>

      <div class="info-plate"></div>

      <div class="foil-band foil-band--bottom" role="img" aria-label="Crinkled gold leaf foil band"></div>
    </section>
  </main>
</body>
</html>
```